New Menu for Elegant Cafe Pastry Shop

We need to choose a design and layout for our new menu. We would like to also condense our current menu to 4-6 pages.
We will be changing prices and items on the menu, so it needs to be editable. Adobe formats are preferred. The size of the pages needs to be letter size. We will be printing it in house
Please take inspiration from the photos of our shop and food and also our Picmosaic page.
Attached are our current menu our logo and the logo info

https://www.picmosaic.com/marbrecoquette/?hl=en
https://maps.wayfindr.app/Qk3Lm9Xp2Tb7VwR4a

Industry/Entity Type

Food Cafe Bakery pastry

Other font styles liked:
• please look at attached files

Colors

Designer to choose colors to be used in the design.

Requirements
Nice to have
• Use of Arches like on our shop wallpaper or oblong eclair shapes, Art Deco elements

```html
<!DOCTYPE html>
<html lang="en">
<head>
<meta charset="utf-8">
<title>Marbre Coquette – Seasonal &amp; Beverages Menu</title>
<link href="https://fonts.googleapis.com/css2?family=Forum&family=Oswald:wght@400;500&family=Montserrat:wght@400&display=swap" rel="stylesheet">
<style>
  :root{
    --backdrop:#000;
    --paper:#ffffff;
    --ink:#2b1820;
    --teal:#45c1cb;
    --nut-blue:#1f4fa8;
    --gf-red:#d4232a;
    --vegan-green:#2e8b3a;
  }
  *{margin:0;padding:0;box-sizing:border-box}
  html,body{width:1200px;height:2320px;overflow:hidden;background:var(--backdrop)}
  .page{position:absolute;left:184px;width:832px;height:1077px;background:var(--paper);color:var(--ink)}
  .page--seasonal{top:61px}
  .page--drinks{top:1178px}
  .abs{position:absolute;white-space:nowrap}
  .display{font-family:"Forum",serif;font-weight:400;color:var(--ink);line-height:1}
  .item{font-family:"Oswald",sans-serif;font-weight:500;text-transform:uppercase;color:var(--ink);line-height:1}
  .body{font-family:"Montserrat",sans-serif;font-size:13.5px;line-height:19px;letter-spacing:.04em;color:var(--ink)}
  .tag{color:var(--nut-blue)}

  /* brand */
  .brand{left:76px;top:160px;display:flex;align-items:center;gap:14px}
  .brand__dot{width:40px;height:40px;border-radius:50%;background:var(--teal)}
  .brand__name{font-family:"Forum",serif;font-size:30px;color:var(--ink);letter-spacing:.02em}

  .seasonal{left:438px;top:155px;font-size:66px}
  .seasonal__note{left:635px;top:214px;font-family:"Montserrat",sans-serif;font-size:13px;letter-spacing:.06em}
  .soups{left:534px;top:340px;font-size:42px}
  .travel{left:454px;top:480px;font-size:42px}

  .row{position:absolute;display:flex;justify-content:space-between;font-size:17px;white-space:nowrap}
  .travel-list .row{left:439px;width:321px}

  .lorraine{left:73px;top:399px;font-size:17px}
  .lorraine__price{left:317px;top:399px;font-size:17px}
  .opera{left:81px;top:671px;font-size:17px}
  .opera__desc{left:79px;top:700px;width:300px;white-space:normal}

  .baba{left:406px;top:735px;width:426px;height:226px;background:var(--teal)}
  .baba__title{left:53px;top:34px;font-size:42px;color:#fff}
  .baba__note{left:235px;top:77px;font-family:"Oswald",sans-serif;font-size:11px;color:#fff;text-transform:uppercase}
  .baba .row{left:33px;width:321px;color:#fff;font-size:17px;font-weight:400}
  .baba .row span{color:#fff}

  .legend{left:0;width:100%;top:1008px;text-align:center;font-family:"Oswald",sans-serif;font-weight:500;font-size:11px;text-transform:uppercase}

  /* drinks page */
  .mocktails{left:0;width:100%;text-align:center;top:52px;font-size:60px}
  .mock{position:absolute;top:152px;width:190px}
  .mock__name{font-size:28px;margin-bottom:14px;white-space:nowrap}
  .mock .body{font-size:12px;line-height:16.5px}
  .beverages{left:0;width:100%;text-align:center;top:280px;font-size:32px}
  .band{left:0;top:331px;width:832px;height:226px;background:var(--teal)}
  .col{position:absolute}
  .col__head{font-size:27px;margin-bottom:22px;white-space:nowrap}
  .band .col__head,.band .item{color:#fff}
  .list{list-style:none}
  .list li{display:flex;justify-content:space-between;gap:8px;white-space:nowrap;font-family:"Oswald",sans-serif;font-weight:500;font-size:11px;text-transform:uppercase;height:24.4px;line-height:24.4px}
  .list .gap{height:24.4px}
  .band .list li{color:#fff;font-weight:400}
  .syrups{left:0;width:100%;text-align:center;top:568px;font-size:28px}
  .syrups__text{left:0;width:100%;text-align:center;top:611px;font-size:13px;line-height:18px;letter-spacing:.08em}
</style>
</head>
<body>

<section class="page page--seasonal">
  <div class="abs brand"><span class="brand__dot"></span><span class="brand__name">Marbre Coquette</span></div>

  <h1 class="abs display seasonal">Seasonal</h1>
  <p class="abs seasonal__note">Upon availability</p>

  <h2 class="abs display soups">Soups</h2>
  <p class="abs item lorraine">Lorraine</p>
  <p class="abs item lorraine__price">| $6.99</p>

  <h2 class="abs display travel">Travel Cakes V</h2>
  <div class="travel-list">
    <p class="row item" style="top:559px"><span>Banana Pecan <span class="tag">CN</span></span><span>$6.00</span></p>
    <p class="row item" style="top:596px"><span>Banana Walnut <span class="tag">CN</span></span><span>$6.00</span></p>
    <p class="row item" style="top:634px"><span>Banana Chocolate Chips</span><span>$6.00</span></p>
    <p class="row item" style="top:671px"><span>Blueberry</span><span>$6.00</span></p>
  </div>

  <p class="abs item opera">Pistachio Raspberry Opera <span class="tag">CN</span> &nbsp;| $ 8.80</p>
  <p class="abs body opera__desc">Pistachio joconde cake layered with pistachio buttercream, chocolate ganache and raspberry gelée.</p>

  <div class="abs baba">
    <h2 class="abs display baba__title">Baba Au Rhum</h2>
    <p class="abs baba__note">Contain alcohol</p>
    <p class="row item" style="top:117px"><span>Chocolate / Noisetta</span><span>$7.80</span></p>
    <p class="row item" style="top:155px"><span>Vanilla/Orange/Pineapple</span><span>$7.80</span></p>
  </div>

  <p class="abs legend"><span class="tag">(CN)</span> - Contains nuts <span class="tag">(CA)</span> - Contains almonds <span class="tag">(CW)</span> - Contains walnuts <span style="color:var(--gf-red)">(GF)</span> - Gluten free <span style="color:var(--vegan-green)">(V)</span> - Vegan</p>
</section>

<section class="page page--drinks">
  <h1 class="abs display mocktails">Mocktails</h1>

  <div class="mock" style="left:75px">
    <h3 class="display mock__name">Pina Colada</h3>
    <p class="body">A tropical classic mocktail of pineapple and coconut<br>$ 6.30</p>
  </div>
  <div class="mock" style="left:320px">
    <h3 class="display mock__name">Mango Lychee</h3>
    <p class="body">Refreshing mix of lychee and mango<br>$ 6.50</p>
  </div>
  <div class="mock" style="left:591px">
    <h3 class="display mock__name">Shirley Temple</h3>
    <p class="body">Ginger ale and grenadine mocktail garnished with maraschino cherry.<br>$ 6.30</p>
  </div>

  <h2 class="abs display beverages">Coffees &amp; Beverages</h2>

  <div class="abs band">
    <div class="col" style="left:75px;top:10px;width:151px">
      <h3 class="display col__head">Iced Coffee</h3>
      <ul class="list"><li><span>Iced Espresso</span><span>$4.00</span></li><li><span>Iced Cappuccino</span><span>$4.55</span></li><li><span>Iced Latte</span><span>$4.75</span></li></ul>
    </div>
    <div class="col" style="left:320px;top:10px;width:179px">
      <h3 class="display col__head">Hot Coffee</h3>
      <ul class="list"><li><span>Filter Coffee</span><span>$2.40</span></li><li><span>Espresso</span><span>$2.75</span></li><li><span>Cappuccino</span><span>$3.50</span></li><li><span>Latte</span><span>$3.70</span></li><li><span>Americano</span><span>$3.00</span></li><li><span>Espresso Macchiato</span><span>$3.00</span></li></ul>
    </div>
    <div class="col" style="left:591px;top:10px;width:149px">
      <h3 class="display col__head">Matcha</h3>
      <ul class="list"><li><span>Matcha Tea</span><span>$3.20</span></li><li><span>Matcha Latte Hot</span><span>$3.95</span></li><li><span>Matcha Latte Cold</span><span>$3.95</span></li></ul>
    </div>
  </div>

  <h2 class="abs display syrups">Syrups - Sauces - Toppings</h2>
  <p class="abs body syrups__text">vanilla | hazelnut | caramel | mocha | lavender | almond (ask for our sugar free options) +$1.00<br>dark or white chocolate sauce+$1.00 extra shot +$1.00 Decaf +$1.00</p>

  <div class="col" style="left:75px;top:700px;width:162px">
    <h3 class="display col__head">Cold Drinks</h3>
    <ul class="list"><li><span>Isla Water 16 oz</span><span>$3.70</span></li><li><span>San Vitale</span><span>$4.70</span></li><li><span>Cola Rossa / Diet</span><span>$4.00</span></li><li><span>Pétillante</span><span>$4.70</span></li><li class="gap"></li><li><span>Homemade Lemonade</span><span>$6.50</span></li><li><span>Mint Lemonade</span><span>$6.50</span></li><li><span>Strawberry Lemonade</span><span>$6.50</span></li><li><span>Lavender Lemonade</span><span>$6.50</span></li><li><span>Orange Juice</span><span>$4.70</span></li></ul>
  </div>
  <div class="col" style="left:320px;top:700px;width:190px">
    <h3 class="display col__head">Tea</h3>
    <ul class="list"><li><span>Earl Grey</span><span>$3.50</span></li><li><span>Darjeeling</span><span>$3.50</span></li><li><span>Ginger Lemongrass</span><span>$3.50</span></li><li><span>Camomile</span><span>$3.50</span></li><li><span>Mint Vervain &amp; Herbs</span><span>$3.50</span></li><li><span>Fruit Symphony</span><span>$3.50</span></li><li><span>Dragon Sencha Green Tea</span><span>$3.50</span></li><li><span>Iced Tea</span><span>$3.50</span></li></ul>
  </div>
  <div class="col" style="left:591px;top:700px;width:132px">
    <h3 class="display col__head">Chocolate</h3>
    <ul class="list"><li><span>Chocolate Hot</span><span>$4.95</span></li><li><span>Chocolate Cold</span><span>$4.95</span></li><li><span>Whipped Cream</span><span>+$1.00</span></li></ul>
  </div>
</section>

</body>
</html>
```